PELDRAX Business Cards

We require a business card for our company that provides IT consulting services. We already have a logo that needs to be used on the card. We want a clean professional looking design that incorporates our colours. Our main focus is providing managed services to business, which involves us looking after all of their IT requirements including managing servers/networks, projects, and procurement.

Industry/Entity Type

Information Technology

Requirements
Must have
• our logo, contact information, name, title, phone numbers

```html
<!DOCTYPE html>
<html lang="en">
<head>
<meta charset="utf-8">
<title>PELDRAX Business Cards</title>
<link href="https://fonts.googleapis.com/css2?family=Lato:wght@400;700;900&display=swap" rel="stylesheet">
<style>
  :root {
    --brand-blue: #0796cf;
    --ink: #3d3f42;
    --card: #f9fafa;
    --backdrop: #eceeef;
    --rule: #9cc9e4;
  }
  html, body {
    margin: 0;
    padding: 0;
    width: 1200px;
    height: 1200px;
    overflow: hidden;
    background: var(--backdrop);
    font-family: "Lato", sans-serif;
  }
  .canvas {
    position: relative;
    width: 1200px;
    height: 1200px;
  }
  .card {
    position: absolute;
    left: 246px;
    width: 708px;
    height: 404px;
    background: var(--card);
  }
  .card--front { top: 138px; }
  .card--back { top: 646px; }

  .wordmark {
    position: absolute;
    display: flex;
    align-items: center;
    color: var(--brand-blue);
    font-weight: 900;
    line-height: 1;
    letter-spacing: 0.02em;
  }
  .wordmark__dot {
    border-radius: 50%;
    background: var(--brand-blue);
    flex: none;
  }
  .card--front .wordmark {
    left: 0; right: 0; top: 150px;
    justify-content: center;
    font-size: 80px;
    gap: 26px;
  }
  .card--front .wordmark__dot { width: 64px; height: 64px; }

  .card--back .wordmark {
    left: 88px; top: 196px;
    font-size: 40px;
    gap: 14px;
  }
  .card--back .wordmark__dot { width: 34px; height: 34px; }

  .divider {
    position: absolute;
    left: 354px;
    top: 116px;
    width: 1px;
    height: 174px;
    background: var(--rule);
  }
  .contact {
    position: absolute;
    left: 378px;
    top: 92px;
    color: var(--ink);
  }
  .contact__name {
    margin: 0;
    font-size: 29px;
    font-weight: 700;
    color: var(--brand-blue);
    line-height: 1;
  }
  .contact__title {
    margin: 8px 0 0;
    font-size: 17px;
    font-weight: 700;
    line-height: 1;
  }
  .contact__address {
    margin: 20px 0 0;
    font-size: 16px;
    line-height: 25px;
    font-style: normal;
  }
  .contact__list {
    list-style: none;
    margin: 16px 0 0;
    padding: 0;
    font-size: 16.5px;
    line-height: 24px;
  }
  .contact__item {
    display: flex;
    align-items: center;
    gap: 12px;
  }
  .contact__icon {
    width: 14px;
    height: 14px;
    flex: none;
    fill: var(--brand-blue);
  }
  .contact__accent { color: var(--brand-blue); }
</style>
</head>
<body>
<main class="canvas">
  <section class="card card--front" aria-label="Card front">
    <div class="wordmark"><span class="wordmark__dot"></span>PELDRAX</div>
  </section>

  <section class="card card--back" aria-label="Card back">
    <div class="wordmark"><span class="wordmark__dot"></span>PELDRAX</div>
    <div class="divider"></div>
    <div class="contact">
      <h1 class="contact__name">Daniel Arbeloa</h1>
      <p class="contact__title">Manager</p>
      <address class="contact__address">Calle del Roble 14<br>Oficina 2B, 31008, Tudela.</address>
      <ul class="contact__list">
        <li class="contact__item">
          <svg class="contact__icon" viewBox="0 0 24 24" aria-hidden="true"><path d="M6.6 10.8a15.1 15.1 0 0 0 6.6 6.6l2.2-2.2c.3-.3.7-.4 1-.2 1.1.4 2.3.6 3.6.6.6 0 1 .4 1 1V20c0 .6-.4 1-1 1A17 17 0 0 1 3 4c0-.6.4-1 1-1h3.5c.6 0 1 .4 1 1 0 1.3.2 2.5.6 3.6.1.3 0 .7-.2 1z"/></svg>
          <span>+34 900 418 273</span>
        </li>
        <li class="contact__item">
          <svg class="contact__icon" viewBox="0 0 24 24" aria-hidden="true"><path d="M2 5h20v14H2z M3 6l9 7 9-7" fill="var(--brand-blue)" stroke="var(--card)" stroke-width="1.5"/></svg>
          <span>hello@peldrax.com</span>
        </li>
        <li class="contact__item">
          <svg class="contact__icon" viewBox="0 0 24 24" aria-hidden="true" fill="none" stroke="#7fa9c8" stroke-width="1.6"><circle cx="12" cy="12" r="9.5"/><ellipse cx="12" cy="12" rx="4.5" ry="9.5"/><path d="M2.5 12h19M4 7h16M4 17h16"/></svg>
          <span>www.<span class="contact__accent">peldrax</span>.com</span>
        </li>
      </ul>
    </div>
  </section>
</main>
</body>
</html>
```